We're Hiring Poster or Flyer design

We’re Hiring Details:

Positions include:
Office Manager
Office Assistant
Data Entry Techs
Outreach Manager
Asst. Outreach Manager
Events Coordinator
Drivers (must have personal car, insurance & Driver’s License)
Outreach Specialist—Walkers
Outreach Specialist—Phone/Telemarketing (evenings only)

Excellent Pay ! Fun Atmosphere ! Bonus Pay with Promotional & Career Advancement Opportunities

***************
need 3 formats of SAME flyer:
1) 8.5 x 11
2) 8.5 x 14
3) 11 x17

creative and eye catching a must; this flyer will be used on college bulletin boards and used to attract a younger demographic . . hip and chic look with "Americana style or political motif" preferred.

Target Market(s)

younger demographic . . flyer will be used during college recruiting fairs and in younger settings---age BRACKET is 21 - 35 Years old

Industry/Entity Type

Employment Agency

Font styles to use
Sans Serif

Colors

Designer to choose colors to be used in the design.

Requirements
Must have
• clean and attractive; hip; chic; simple and with good stock pics and layout
Nice to have
• american flag and patriotism
Should not have
• too much details on the job -- I only included the job announcement so you can get an idea of WHAT and WHO I am looking for . . don't list all the BORING details on the flyer/poster

```html
<!DOCTYPE html>
<html lang="en">
<head>
<meta charset="utf-8">
<title>Now Hiring – Jordan Calloway</title>
<link rel="stylesheet" href="https://fonts.googleapis.com/css2?family=Oswald:wght@500;600;700&display=swap">
<style>
  :root{
    --navy:#1a2a78;
    --navy-deep:#0f1b5c;
    --poster-red:#d3132f;
    --white:#ffffff;
    --ink:#111111;
    --skin:#e0a88a;
    --shirt:#3f76c4;
  }
  *{margin:0;padding:0;box-sizing:border-box}
  html,body{width:947px;height:1200px;overflow:hidden;background:var(--white)}
  .flyer{position:relative;width:947px;height:1200px;overflow:hidden;
    font-family:"Oswald",sans-serif;color:var(--white);background:var(--navy)}

  .top-band{position:absolute;left:0;top:0;width:947px;height:678px;
    background:linear-gradient(180deg,var(--navy) 0%,var(--navy-deep) 100%)}
  .flag-backdrop{position:absolute;left:0;top:0;width:947px;height:400px;
    background:linear-gradient(170deg,#2c3f8f 0%,#5a6aa8 18%,#24357f 34%,#a9485a 48%,#2a3a86 62%,rgba(26,42,120,0) 100%);
    opacity:.9}
  .divider{position:absolute;left:0;top:678px;width:947px;height:16px;background:var(--white)}
  .bottom-band{position:absolute;left:0;top:694px;width:947px;height:506px;background:var(--poster-red)}

  .stamp{position:absolute;left:70px;top:88px;width:395px;height:100px;z-index:2;
    background:var(--white);border:6px solid var(--ink);outline:4px solid var(--white);
    transform:rotate(-9deg);display:flex;align-items:center;justify-content:center}
  .stamp span{font-weight:700;font-size:66px;letter-spacing:1px;color:var(--ink);line-height:1}

  .tagline{position:absolute;left:90px;top:262px;width:340px;z-index:2;
    transform:rotate(-8deg);transform-origin:left top;
    font-weight:600;font-size:24px;line-height:34px}

  .hero-photo{position:absolute;left:40px;top:410px;width:480px;height:268px;z-index:1;
    border-radius:150px 150px 0 0;
    background:radial-gradient(ellipse at 55% 30%,var(--skin) 0%,#b77a5e 30%,var(--shirt) 60%,#2c5ca6 85%,rgba(44,92,166,0) 100%)}
  .hero-hand{position:absolute;left:380px;top:694px;width:190px;height:140px;z-index:1;
    border-radius:0 0 90px 40px;
    background:linear-gradient(200deg,#2c5ca6 0%,var(--skin) 55%,rgba(224,168,138,.6) 100%)}

  .positions{position:absolute;left:497px;top:160px;list-style:none;z-index:3}
  .positions li{position:relative;padding-left:24px;font-weight:600;font-size:30px;line-height:39px;white-space:nowrap}
  .positions li::before{content:"";position:absolute;left:2px;top:17px;width:8px;height:8px;border-radius:50%;background:var(--white)}
  .positions small{font-size:21px;font-weight:600}
  .positions .wrap{display:block;font-size:21px;line-height:30px}

  .apply-box{position:absolute;left:94px;top:832px;width:262px;height:84px;
    border:3px solid var(--white);border-radius:10px}
  .apply-kicker{position:absolute;left:60px;top:818px;font-weight:600;font-size:27px;line-height:30px;
    background:var(--poster-red);padding-right:8px}
  .apply-arrow{position:absolute;left:88px;top:858px;background:var(--poster-red)}
  .apply-word{position:absolute;left:125px;top:844px;font-weight:700;font-size:56px;line-height:62px;letter-spacing:8px}

  .contact{position:absolute;left:82px;top:938px;font-weight:600;font-size:29px;line-height:37.5px}
  .contact .small{font-size:27px}

  .candidate{position:absolute;left:530px;top:925px;width:340px;text-align:center;
    font-weight:700;font-size:52px;line-height:1.1;color:var(--white)}
  .site{position:absolute;left:541px;top:1080px;width:340px;text-align:center;font-weight:600;font-size:26px}
</style>
</head>
<body>
<main class="flyer">
  <div class="top-band"></div>
  <div class="flag-backdrop" role="img" aria-label="Waving American flag photograph"></div>

  <div class="stamp"><span>NOW HIRING</span></div>
  <p class="tagline">Excellent Pay ! Fun<br>Atmosphere ! Bonus Pay with<br>Promotional &amp; Career<br>Advancement Opportunities</p>

  <div class="divider"></div>
  <div class="bottom-band"></div>

  <div class="hero-photo" role="img" aria-label="Photo of a smiling young man in a blue shirt giving a thumbs up"></div>
  <div class="hero-hand" role="img" aria-label="The man's hand pointing down toward the application details"></div>

  <ul class="positions">
    <li>Office Manager</li>
    <li>Office Assistant</li>
    <li>Data Entry Techs</li>
    <li>Outreach Manager</li>
    <li>Asst. Outreach Manager</li>
    <li>Events Coordinator</li>
    <li>Drivers <small>(must have personal car,</small><span class="wrap">insurance &amp; Driver’s License)</span></li>
    <li>Outreach Specialist—Walkers</li>
    <li>Outreach Specialist—Phone</li>
    <li>Telemarketing <small>(evenings only)</small></li>
  </ul>

  <div class="apply-box"></div>
  <span class="apply-kicker">» HOW TO</span>
  <svg class="apply-arrow" width="14" height="56" viewBox="0 0 14 56" aria-hidden="true">
    <path d="M7 54 V4 M1 12 L7 3 L13 12" fill="none" stroke="#fff" stroke-width="3"/>
  </svg>
  <span class="apply-word">APPLY</span>

  <p class="contact">
    Email resume PRIOR to phone<br>
    <span class="small">screening, to: j.2015@mailbox.com</span><br>
    Call for telephone screening:<br>
    909-555-0148
  </p>

  <p class="candidate">Jordan Calloway</p>
  <p class="site">CALLOWAYFORMAYOR.COM</p>
</main>
</body>
</html>
```